Business Card Design - Crisp & Clean

Looking for a new clean and crisp business card design. Design must incorporate our corporate colors (see attached style sheet). We're a pretty fun loving group who likes to keep it light while still portraying a professional image. Card should incorporate both our logo and our mascot (see attachment). Card should be double sided and should have room for our social media - Facebook, Linked In and Twitter on the back. Font selections do not have to match the style guide.

```html
<!DOCTYPE html>
<html lang="en">
<head>
<meta charset="utf-8">
<title>BrightCrew HR – Business Cards</title>
<link rel="stylesheet" href="https://fonts.googleapis.com/css2?family=Open+Sans:wght@400;600;700&display=swap">
<style>
  :root {
    --page: #ecebe8;
    --gold: #f3b21b;
    --gold-deep: #d8940c;
    --brown-dark: #3a2b10;
    --brown-mid: #7a5a16;
    --ink: #1b1b1b;
    --white: #ffffff;
    --shadow: rgba(0, 0, 0, 0.18);
  }
  * { box-sizing: border-box; margin: 0; padding: 0; }
  html, body {
    width: 1200px; height: 784px; overflow: hidden;
    background: var(--page);
    font-family: "Open Sans", sans-serif;
  }
  .sheet {
    width: 1200px; height: 784px;
    display: flex; align-items: center; justify-content: center; gap: 40px;
  }
  .card {
    position: relative;
    width: 540px; height: 309px;
    border-radius: 4px;
    overflow: hidden;
    box-shadow: 0 10px 24px var(--shadow);
  }

  /* Back side */
  .card--back {
    background: linear-gradient(120deg, var(--brown-dark) 0%, var(--brown-mid) 55%, var(--gold-deep) 100%);
    color: var(--white);
  }
  .card--back .pattern-area {
    position: absolute; inset: 0 0 0 38%;
    background: radial-gradient(ellipse at 70% 50%, rgba(243,178,27,0.55), rgba(243,178,27,0.08) 70%);
  }
  .card--back .mascot {
    position: absolute; right: 40px; top: 34px;
    width: 150px; height: 160px; border-radius: 50%;
    background: radial-gradient(circle at 50% 45%, #ffd75a, var(--gold) 60%, var(--gold-deep));
  }
  .brand {
    position: absolute; left: 34px; top: 36px;
    display: flex; align-items: center; gap: 12px;
  }
  .brand__dot {
    width: 44px; height: 44px; border-radius: 50%;
    background: var(--gold);
  }
  .brand__name {
    font-weight: 700; font-size: 27px; letter-spacing: -0.3px;
  }
  .card--back .brand__name { color: var(--white); }
  .social {
    position: absolute; left: 30px; top: 192px;
    list-style: none;
  }
  .social__item {
    display: flex; align-items: center; gap: 8px;
    font-size: 15.5px; line-height: 22px; font-weight: 400;
  }
  .social__icon {
    width: 14px; height: 14px; border-radius: 2px;
    background: var(--white); opacity: 0.85;
  }

  /* Front side */
  .card--front { background: var(--white); color: var(--ink); }
  .card--front .brand__name { color: var(--ink); }
  .card--front .faint-mark {
    position: absolute; right: -30px; top: 70px;
    width: 190px; height: 190px; border-radius: 50%;
    background: var(--gold); opacity: 0.12;
  }
  .person { position: absolute; left: 34px; top: 160px; }
  .person__name { color: var(--gold); font-weight: 700; font-size: 19px; }
  .person__title { font-size: 14px; margin-top: 4px; }
  .contact {
    position: absolute; left: 34px; top: 226px;
    list-style: none;
  }
  .contact__item {
    display: flex; align-items: center; gap: 8px;
    font-size: 17px; line-height: 23px;
  }
  .contact__icon { width: 15px; height: 15px; flex: none; }
</style>
</head>
<body>
<main class="sheet">
  <section class="card card--back" aria-label="Card back">
    <div class="pattern-area" role="img" aria-label="Soft pattern of golden ovals"></div>
    <div class="mascot" role="img" aria-label="Mascot illustration: cartoon professor holding a light bulb"></div>
    <div class="brand">
      <span class="brand__dot"></span>
      <span class="brand__name">BrightCrew HR</span>
    </div>
    <ul class="social">
      <li class="social__item"><span class="social__icon"></span>brightcrewhrsolutions</li>
      <li class="social__item"><span class="social__icon"></span>brightcrewhrsolutions</li>
      <li class="social__item"><span class="social__icon"></span>brightcrewhrsolutions</li>
    </ul>
  </section>

  <section class="card card--front" aria-label="Card front">
    <div class="faint-mark"></div>
    <div class="brand">
      <span class="brand__dot"></span>
      <span class="brand__name">BrightCrew HR</span>
    </div>
    <div class="person">
      <p class="person__name">Maren Holt</p>
      <p class="person__title">Marketing Wizard</p>
    </div>
    <ul class="contact">
      <li class="contact__item">
        <svg class="contact__icon" viewBox="0 0 16 16" aria-hidden="true"><path d="M3 1.5l2.5 0 1.2 3-1.6 1.2a8 8 0 0 0 5.2 5.2l1.2-1.6 3 1.2v2.5a1.5 1.5 0 0 1-1.6 1.5A12.5 12.5 0 0 1 1.5 3.1 1.5 1.5 0 0 1 3 1.5z" fill="var(--gold-deep)"/></svg>
        555-014-2290
      </li>
      <li class="contact__item">
        <svg class="contact__icon" viewBox="0 0 16 16" aria-hidden="true"><rect x="1" y="3" width="14" height="10" rx="1.5" fill="var(--gold-deep)"/><path d="M1.5 4l6.5 5 6.5-5" stroke="#fff" stroke-width="1.3" fill="none"/></svg>
        maren@brightcrewhr.com
      </li>
      <li class="contact__item">
        <svg class="contact__icon" viewBox="0 0 16 16" aria-hidden="true"><circle cx="8" cy="8" r="7" fill="var(--gold-deep)"/><g stroke="#fff" stroke-width="1" fill="none"><ellipse cx="8" cy="8" rx="3" ry="7"/><path d="M1 8h14M2.5 4.5h11M2.5 11.5h11"/></g></svg>
        www.brightcrewhr.com
      </li>
    </ul>
  </section>
</main>
</body>
</html>
```